Presentation card Venture KELO - Tech Incubator from Perú

We need a Design to promote the incubator of technology Startups.
We are in Perú, we work with a string tech filter and develop enterprenurship competencies in the Startup team.
The card is to facilitators and staff memebers of VentureKELO.
We want a clear, modern, tech and agile Design.

We work to help New enterprises of technology here in Perú, we expect the candidates have a big competencies to Research and develop technological products.

We work using methodologies from QRB, Folmestry, Brakewell and Harrowgate univeesities. Our book base is the disciplina of enterpreneur.

We work events all year using diferent formats: Brightforge, Vorne price, OPRA Model Competition you can use these logros in your Design.

Set the name, role, email, cell phone number, address.

Example:
// Contact info section
Tobías Quiroveda
Swift Modeling Hub Manager
tobias.quiroveda@kelo-example.pe
(511) 999 000 417

// Address info section
VentureKELO
Technology-based business incubator
Av. Los Cedrales 884, Valdora
Lima - Perú
web: venture-kelo-example.org.pe
email: venture@kelo-example.pe
phone number: (511) 3926508 ext. 4418

// (optional)Lema section
Making happy using technology

// Social network section
facebook: venturekelooficial

Target Market(s)

Enterprenurship, CTO, Investors, Companies interested on open innovation services

Industry/Entity Type

Information Technology

Contact Information for Business Card

Name, Role, Email, Cell phone number

Colors

Designer to choose colors to be used in the design.

Requirements
Must have
• Logo forms and colors
Nice to have
• I add pictures of the leaders of incubator
Should not have
• No vertical designs

```html
<!DOCTYPE html>
<html lang="en">
<head>
<meta charset="utf-8">
<title>Venture KELO – Business Card</title>
<link href="https://fonts.googleapis.com/css2?family=Nunito+Sans:wght@300;400;600;800;900&display=swap" rel="stylesheet">
<style>
  :root {
    --magenta: #bd335b;
    --arc-grey: #e1e1e4;
    --ink: #1d1d1f;
    --paper: #ffffff;
    --backdrop: #d6d5d1;
  }
  * { margin: 0; padding: 0; box-sizing: border-box; }
  html, body { width: 1200px; height: 820px; overflow: hidden; }
  body {
    background: var(--backdrop);
    font-family: "Nunito Sans", sans-serif;
    color: var(--ink);
    position: relative;
  }
  .card {
    position: absolute;
    left: 290px;
    width: 620px;
    height: 370px;
    background: var(--paper);
    overflow: hidden;
  }
  .card--front { top: 25px; }
  .card--back { top: 425px; }
  .card-shapes { position: absolute; inset: 0; }

  /* Front */
  .brand-name {
    position: absolute;
    left: 24px;
    top: 44px;
    font-weight: 900;
    font-size: 36px;
    line-height: 1;
    color: var(--ink);
    white-space: nowrap;
  }
  .tagline {
    position: absolute;
    left: 343px;
    top: 34px;
    font-weight: 900;
    font-size: 27px;
    line-height: 1.2;
  }
  .tagline-accent { color: var(--magenta); display: block; }
  .address {
    position: absolute;
    left: 24px;
    top: 218px;
    font-size: 14.5px;
    line-height: 1.3;
  }
  .contact-list {
    position: absolute;
    left: 23px;
    top: 264px;
    list-style: none;
    font-size: 14.5px;
  }
  .contact-list li { height: 22px; display: flex; align-items: center; gap: 3px; }
  .contact-list .phone-line { font-size: 13px; }
  .contact-label { color: var(--magenta); font-weight: 800; }
  .social-dot {
    width: 14px; height: 14px; border-radius: 50%;
    background: #3b5b9a; margin-right: 8px;
  }
  .motto {
    position: absolute;
    right: 31px;
    top: 272px;
    text-align: right;
    color: var(--paper);
    font-weight: 300;
    font-size: 27px;
    line-height: 1.1;
  }

  /* Back */
  .person-name {
    position: absolute;
    left: 0; right: 0;
    top: 218px;
    text-align: center;
    font-weight: 800;
    font-size: 27px;
  }
  .person-name .surname { color: var(--magenta); }
  .person-role {
    position: absolute;
    left: 0; right: 0;
    top: 253px;
    text-align: center;
    color: var(--magenta);
    font-size: 18px;
  }
  .person-contact {
    position: absolute;
    left: 0; right: 0;
    top: 283px;
    text-align: center;
    font-size: 18px;
    line-height: 1.25;
    letter-spacing: 0.3px;
  }
</style>
</head>
<body>

<section class="card card--front" aria-label="Business card front">
  <svg class="card-shapes" viewBox="0 0 620 370" aria-hidden="true">
    <path d="M272 370 C 350 245 470 168 620 162 L620 370 Z" fill="var(--arc-grey)"/>
    <path d="M279 370 C 360 262 470 192 620 188 L620 370 Z" fill="var(--magenta)"/>
  </svg>

  <p class="brand-name">Venture KELO</p>

  <h2 class="tagline">Technology-based <span class="tagline-accent">business incubator</span></h2>

  <p class="address">Av. Los Cedrales 884, Valdora<br>Lima - Perú</p>

  <ul class="contact-list">
    <li><span class="contact-label">e:</span> venture@kelo-example.pe</li>
    <li><span class="contact-label">w:</span> venture-kelo-example.org.pe</li>
    <li class="phone-line"><span class="contact-label">p:</span> (511) 3926508 ext. 4418</li>
    <li><span class="social-dot"></span>venturekelooficial</li>
  </ul>

  <p class="motto">Making happy<br>using technology</p>
</section>

<section class="card card--back" aria-label="Business card back">
  <svg class="card-shapes" viewBox="0 0 620 370">
    <defs>
      <radialGradient id="portraitTone" cx="50%" cy="40%" r="60%">
        <stop offset="0" stop-color="#c79a7c"/>
        <stop offset="1" stop-color="#3d3b4a"/>
      </radialGradient>
      <linearGradient id="teamTone" x1="0" y1="0" x2="1" y2="1">
        <stop offset="0" stop-color="#d9d7d2"/>
        <stop offset="0.45" stop-color="#2c3447"/>
        <stop offset="1" stop-color="#6b5a4a"/>
      </linearGradient>
      <clipPath id="portraitClip">
        <path d="M0 0 H265 C 240 110 150 185 0 200 Z"/>
      </clipPath>
    </defs>
    <circle cx="102" cy="105" r="95" fill="url(#portraitTone)" clip-path="url(#portraitClip)"
            role="img" aria-label="Portrait photo of the team member"/>
    <path d="M0 240 C 150 205 255 140 270 0 L 266 0 C 240 125 150 195 0 238 Z" fill="var(--arc-grey)"/>
    <path d="M272 0 C 300 110 430 225 620 218 L620 0 Z" fill="url(#teamTone)"
          role="img" aria-label="Group photo of the incubator team in a workshop room"/>
    <rect x="0" y="353" width="620" height="17" fill="var(--arc-grey)"/>
    <path d="M0 353 H395 C 388 356 384 363 381 370 H0 Z" fill="var(--magenta)"/>
  </svg>

  <h1 class="person-name">Tobías <span class="surname">Quiroveda</span></h1>
  <p class="person-role">Swift Modeling Hub Manager</p>
  <p class="person-contact">tobias.quiroveda@kelo-example.pe<br>(511) 999 000 417</p>
</section>

</body>
</html>
```